We need a poster designed for use on facebook, as well as to print out for advertising in local noticeboards and shop windows.
The poster will advertise the Fernhollow Turf Society 30th Anniversary Ball.
the ball will be held on the 28th April 2018 at the Fernhollow Community Hall.
Time will be 630pm till late. Ticket Price is $120 which includes 3 course dinner, drinks on arrival and entertainment during the evening.
Additional details will need to be added to the poster at a later date.
The fernhollow Turf Society is a horse racing club run by the community. The club has been incorporateds for 30 years. This Ball will be a celebration of that anniversary.

Target Market(s)

Middlemount Community

Industry/Entity Type

Club

Font styles to use
Serif
Decorative

Colors
1b1b1b
fbfbfb
6b449b
886aae
a64599
ffc214

Requirements
Must have
• Include
• where when time and cost
• ticket inclusions
• entertainement by Colin Hartwell
Nice to have
• Attached are some images for inspiration.
• It would be nice to have the race club logo included somewhere however not prominant.
Should not have
• Abstract geometriic lines
• images of people
• primary colours

```html
<!DOCTYPE html>
<html lang="en">
<head>
<meta charset="utf-8">
<title>Fernhollow Turf Society 30th Anniversary Ball</title>
<link rel="stylesheet" href="https://fonts.googleapis.com/css2?family=Cinzel:wght@400;500&family=Pinyon+Script&display=swap">
<style>
  :root {
    --backdrop: #ededed;
    --paper: #ffffff;
    --ink: #1b1b1b;
    --gold: #c9962f;
    --gold-light: #f0d48a;
    --gold-deep: #a8771c;
    --serif: "Cinzel", "Times New Roman", serif;
    --script: "Pinyon Script", "Brush Script MT", cursive;
  }
  * { margin: 0; padding: 0; box-sizing: border-box; }
  html, body { width: 1200px; height: 1000px; overflow: hidden; background: var(--backdrop); }
  .canvas { position: relative; width: 1200px; height: 1000px; }
  .poster {
    position: absolute; left: 268px; top: 12px; width: 684px; height: 976px;
    background: var(--paper); color: var(--ink); font-family: var(--serif);
  }
  .frame { position: absolute; left: 0; top: 0; }
  .floral { position: absolute; border-radius: 40%; }
  .floral--top-left {
    left: 18px; top: 22px; width: 310px; height: 320px;
    background: radial-gradient(ellipse at 35% 35%, #f3e2b8 0%, #f8eed6 45%, rgba(255,255,255,0) 72%);
  }
  .floral--bottom-right {
    left: 362px; top: 642px; width: 312px; height: 326px;
    background: radial-gradient(ellipse at 62% 62%, #f3e2b8 0%, #f8eed6 45%, rgba(255,255,255,0) 72%);
  }
  .club-mark {
    position: absolute; left: 0; width: 100%; top: 150px;
    display: flex; justify-content: center; align-items: center; gap: 6px;
    padding-left: 32px; font-size: 9px; letter-spacing: 0.5px; color: var(--gold-deep);
  }
  .club-mark__dot { width: 10px; height: 10px; border-radius: 50%; background: var(--gold); }
  .title-block { position: absolute; left: 178px; width: 360px; top: 206px; text-align: center; }
  .club-name { font-size: 23px; letter-spacing: 0.3px; line-height: 32px; }
  .milestone {
    font-family: var(--script); font-size: 190px; line-height: 150px; height: 150px;
    background: linear-gradient(100deg, var(--gold-deep) 0%, var(--gold-light) 40%, var(--gold) 65%, var(--gold-deep) 100%);
    -webkit-background-clip: text; background-clip: text; color: transparent;
    margin-left: -10px;
  }
  .event-name {
    border-top: 1.5px solid var(--ink); border-bottom: 1.5px solid var(--ink);
    font-size: 32px; line-height: 36px; padding-top: 1px; letter-spacing: 0.5px;
  }
  .details { position: absolute; left: 178px; width: 360px; top: 503px; text-align: center; }
  .details__date {
    display: inline-block; font-size: 23px; line-height: 28px;
    border-bottom: 1.5px solid var(--ink); word-spacing: 3px;
  }
  .details__time { font-size: 17px; line-height: 24px; }
  .details__venue { font-family: var(--script); font-size: 22px; line-height: 22px; }
  .inclusions { position: absolute; left: 150px; width: 410px; top: 657px; text-align: center; font-size: 11.5px; line-height: 18px; }
  .ticket { position: absolute; left: 190px; width: 300px; top: 758px; text-align: center; }
  .ticket__label { font-size: 15px; line-height: 22px; }
  .ticket__price { font-size: 14px; color: var(--gold); line-height: 22px; }
</style>
</head>
<body>
<div class="canvas">
  <article class="poster">
    <svg class="frame" width="684" height="976" viewBox="0 0 684 976" aria-hidden="true">
      <g fill="none" stroke="#c9962f" stroke-width="1.4">
        <polyline points="332,70 626,70 626,608"/>
        <polyline points="62,350 62,904 342,904"/>
      </g>
    </svg>
    <div class="floral floral--top-left" role="img" aria-label="Gold line-art flowers and leaves in the upper left corner"></div>
    <div class="floral floral--bottom-right" role="img" aria-label="Gold line-art flowers and leaves in the lower right corner"></div>

    <div class="club-mark"><span class="club-mark__dot"></span><span>Fernhollow Turf Society</span></div>

    <header class="title-block">
      <p class="club-name">FERNHOLLOW TURF SOCIETY</p>
      <p class="milestone">30th</p>
      <h1 class="event-name" style="font-weight:400">ANNIVERSARY BALL</h1>
    </header>

    <section class="details">
      <p class="details__date">FRIDAY&nbsp; 28TH APRIL 2018</p>
      <p class="details__time">AT SIX THIRTY IN THE EVENING</p>
      <p class="details__venue">Fernhollow Community Hall</p>
    </section>

    <p class="inclusions">ENJOY 3 COURSE DINNER, DRINKS ON ARRIVAL<br>AND ENTERTAINMENT DURING THE EVENING.</p>

    <section class="ticket">
      <p class="ticket__label">TICKET PRICE</p>
      <p class="ticket__price">$120</p>
    </section>
  </article>
</div>
</body>
</html>
```